BenefitGavelHub Website Redesign

I'm looking to give our website a new look and feel with better graphics/images and that is focused on conversions.
www.benefitgavelhub.example. The content can stay the same. Im looking for a new hero section with maybe a call to auction form to create an auction by asking for the following information: Event Name, Event Benefits, Country, Time zone and currency.
Our goal is to show that we can host online auctions, mobile auctions and live in-person auction. The content does not need to change on the site. We just need sections or illustrations that represent those features. It would also be good to have a sections that will segment our users into the following categories: Nonprofits/Charities, Schools/Education, Businesses, Government Agency, Individual.
The following pages need to be updated:
https://www.benefitgavelhub.example/
https://www.benefitgavelhub.example/online-bidding-features
https://www.benefitgavelhub.example/online-bidding-experience
https://www.benefitgavelhub.example/about
https://www.benefitgavelhub.example/pricing
Updates
This project would cover the following 4 pages:
https://www.benefitgavelhub.example

```html
<!DOCTYPE html>
<html lang="en">
<head>
<meta charset="utf-8">
<title>BenefitGavelHub – Homepage Concepts</title>
<link href="https://fonts.googleapis.com/css2?family=Montserrat:wght@400;500;600;700&family=Poppins:wght@400;500;600&display=swap" rel="stylesheet">
<style>
:root{
  --board:#6d6e70;
  --blue:#2f7de1;
  --blue-dark:#1d4fa8;
  --navy:#16223a;
  --ink:#1e2532;
  --muted:#6b7280;
  --pale:#eef4fd;
  --soft:#f4f6fa;
  --red:#e0393b;
  --white:#ffffff;
  --black:#07090d;
}
*{box-sizing:border-box;margin:0;padding:0}
html,body{width:1200px;height:3114px;overflow:hidden}
body{background:var(--board);font-family:"Poppins",sans-serif;color:var(--ink);position:relative}
.page{position:absolute;top:69px;width:500px;background:var(--white);overflow:hidden}
.page--form{left:65px}
.page--photo{left:634px}
h2,h3{font-family:"Montserrat",sans-serif;text-transform:uppercase;letter-spacing:.06em;font-weight:500}
.section-title{display:flex;align-items:center;justify-content:center;gap:7px;font-size:14px;color:var(--ink)}
.dot{width:15px;height:15px;border-radius:50%;background:var(--blue);flex:none}
.btn{display:inline-block;background:var(--blue);color:var(--white);font-family:"Montserrat",sans-serif;font-size:6px;font-weight:600;letter-spacing:.05em;text-transform:uppercase;padding:7px 14px;border-radius:3px;white-space:nowrap}
.btn--round{border-radius:14px}
p{font-size:6px;line-height:1.75;color:var(--muted)}

/* nav */
.nav{height:34px;display:flex;align-items:center;padding:0 46px;gap:10px}
.logo{display:flex;align-items:center;gap:5px;font-family:"Poppins",sans-serif;font-weight:600;font-size:11px;color:var(--blue);margin-right:auto}
.logo .dot{width:13px;height:13px}
.nav-links{display:flex;gap:9px;font-size:5.5px;color:var(--ink)}
.search{width:7px;height:7px;border:1.2px solid var(--ink);border-radius:50%}
.nav .btn{padding:5px 8px;font-size:5px;text-transform:none}

/* hero */
.hero{height:249px;position:relative}
.hero-bg{position:absolute;inset:0}
.page--form .hero-bg{background:linear-gradient(120deg,#dce9fb 0%,#b8d2f6 45%,#6ea2ec 80%,#3b82e6 100%)}
.page--photo .hero-bg{background:linear-gradient(100deg,#c8cdd4 0%,#9aa3ad 40%,#6d6a66 70%,#4a4846 100%)}
.hero-copy{position:absolute;left:30px;top:44px;width:262px;text-align:center}
.hero-copy h1{font-family:"Montserrat",sans-serif;font-weight:500;text-transform:uppercase;font-size:15.5px;line-height:1.4;letter-spacing:.05em;color:var(--blue-dark)}
.hero-copy p{color:#4b5a73;margin:12px 14px 0;font-size:5.5px}
.page--photo .hero-copy p{color:#fff}
.hero-actions{display:flex;gap:5px;justify-content:center;margin-top:13px}
.hero-actions .btn{padding:7px 9px;font-size:5px}
.btn--light{background:var(--white);color:var(--blue-dark)}
.btn--navy{background:var(--blue-dark)}
.event-card{position:absolute;left:304px;top:33px;width:152px;height:165px;background:var(--white);border-radius:5px;box-shadow:0 4px 16px rgba(20,50,110,.2);padding:16px 14px}
.event-card h3{font-size:8.5px;text-align:center;margin-bottom:10px;color:var(--ink)}
.field{height:12px;border:1px solid #d6dbe3;border-radius:2px;font-size:4.5px;color:#6b7280;padding:0 5px;display:flex;align-items:center;justify-content:space-between;margin-bottom:7px}
.field::after{content:"";width:3px;height:3px;border-right:1px solid #777;border-bottom:1px solid #777;transform:rotate(45deg)}
.field--text::after{display:none}
.event-card .link{display:block;text-align:center;font-size:4.5px;color:var(--blue);margin-top:6px;letter-spacing:.05em}

/* categories */
.categories{height:132px;padding-top:30px}
.cat-row{display:flex;justify-content:center;gap:14px;margin-top:16px}
.cat{width:72px;height:58px;background:var(--white);border-radius:4px;box-shadow:0 3px 12px rgba(30,60,120,.14);display:flex;flex-direction:column;align-items:center;justify-content:center;gap:4px}
.cat svg{width:22px;height:22px}
.cat span{font-family:"Montserrat",sans-serif;font-size:4.5px;font-weight:600;text-transform:uppercase;text-align:center;line-height:1.3}

/* feature rows */
.spend-title{height:66px;padding-top:36px}
.row{display:flex;align-items:center;gap:24px;padding:0 46px}
.row--b1{height:224px}
.row--b2{height:230px}
.row--b3{height:242px}
.circle{width:200px;height:200px;border-radius:50%;border:1px dashed #cfd6e1;padding:10px;flex:none}
.circle div{width:100%;height:100%;border-radius:50%}
.img-donate{background:linear-gradient(140deg,#9fc2ef,#3d7fd6 60%,#1e3f7a)}
.img-phone{background:linear-gradient(140deg,#c8c3bf,#6e5a55 55%,#2d2523)}
.img-tablet{background:linear-gradient(140deg,#dfe3ea,#a9b2bf 60%,#575f6b)}
.copy{flex:1}
.copy h3{font-size:9.5px;line-height:1.4;color:var(--ink);margin-bottom:8px}
.quote{background:var(--white);box-shadow:0 3px 14px rgba(30,50,90,.13);border-radius:3px;padding:10px 12px 10px 26px;position:relative;margin:12px 0 16px}
.avatar{position:absolute;left:-4px;top:8px;width:22px;height:22px;border-radius:50%;background:linear-gradient(#c8a48a,#7b5a47)}
.stars{color:#f5b40a;font-size:6px;letter-spacing:1px}
.quote p{color:#2a2f3a;font-size:5.2px;margin:3px 0 5px}
.quote .who{font-size:5px;color:var(--ink)}
.quote .who b{font-weight:600}

.kids{background:linear-gradient(180deg,#ffffff 0%,#f7f2ef 35%,#efe2d9 70%,#e8d7cb 100%)}
.company{height:175px;text-align:center;padding-top:28px}
.company .sub{font-size:7px;color:var(--ink);margin-top:6px;letter-spacing:.04em}
.partners{display:flex;justify-content:center;gap:16px;margin-top:16px;align-items:center}
.partner{width:48px;height:48px;border-radius:4px;background:rgba(255,255,255,.55)}
.partner--card{width:66px;height:62px;background:var(--white);box-shadow:0 3px 10px rgba(0,0,0,.15)}
.partner span{display:block;margin:11px auto;width:26px;height:26px;border-radius:50%;background:#c4c9d4}

/* most used */
.features{height:375px;background:var(--soft);padding-top:30px}
.tabs{display:flex;justify-content:center;gap:8px;margin-top:18px}
.tab{font-size:4.5px;font-family:"Montserrat",sans-serif;font-weight:600;text-transform:uppercase;color:var(--blue);background:var(--white);padding:6px 9px;border-radius:2px}
.tab--on{background:var(--blue);color:var(--white)}
.feat-body{display:flex;margin-top:24px}
.diamond{width:240px;height:220px;position:relative;flex:none}
.diamond .shape{position:absolute;left:10px;top:20px;width:160px;height:160px;border-radius:34px;transform:rotate(45deg);background:linear-gradient(135deg,#5aa0f2,#1d5fcc)}
.diamond .photo{position:absolute;left:80px;top:40px;width:135px;height:135px;border-radius:50%;background:linear-gradient(140deg,#e6e3df,#8aa0bd 60%,#2d4c7a)}
.feat-copy{width:200px;margin-left:4px}
.feat-copy h3{font-size:9.5px;margin:6px 0 8px}
.feat-copy p{margin-bottom:9px;font-size:5.3px}

/* faq */
.faq{height:366px;padding-top:40px}
.faq-card{margin:18px auto 0;width:370px;background:var(--white);border-radius:16px;box-shadow:0 4px 20px rgba(30,50,90,.12);padding:18px 20px 26px;position:relative}
.q{display:flex;align-items:center;gap:10px;background:var(--soft);border-radius:14px;height:27px;padding:0 8px;margin-bottom:15px;font-size:7px;font-family:"Montserrat",sans-serif;font-weight:500;letter-spacing:.03em}
.q b{width:20px;height:20px;border-radius:50%;border:2px solid #dbe6f8;background:var(--blue-dark);color:#fff;font-size:7px;display:flex;align-items:center;justify-content:center;flex:none}
.q i{margin-left:auto;font-style:normal;color:var(--blue);font-size:9px}
.q--open{background:none}
.answer{border-left:1px solid #d5dbe5;margin:-6px 0 0 40px;padding-left:10px}
.answer a{color:var(--blue)}
.chev{position:absolute;bottom:-8px;left:50%;margin-left:-8px;width:16px;height:16px;border-radius:50%;background:#fff;box-shadow:0 2px 6px rgba(0,0,0,.12)}

/* support */
.support{height:197px;position:relative;background:linear-gradient(100deg,#2d3542 0%,#4a5160 45%,#a99588 75%,#7d6f69 100%);padding:24px 46px}
.support .dot{width:14px;height:14px}
.support h2{color:#fff;font-size:16px;line-height:1.3;margin:6px 0 8px;width:220px}
.support p{color:#d6dae2;width:200px}
.btn--red{background:var(--red);margin-top:12px}

/* jam */
.jam{height:355px;padding-top:34px;text-align:center}
.jam .section-title{line-height:1.35;font-size:13px}
.jam-grid{display:flex;gap:16px;justify-content:center;margin-top:20px}
.jcard{width:124px;height:190px;background:var(--white);box-shadow:0 3px 14px rgba(30,50,90,.14);border-radius:4px;padding:6px}
.jcard .ph{height:95px;border-radius:3px}
.ph-a{background:linear-gradient(#eceae7,#c7c1bb)}
.ph-b{background:linear-gradient(#c6ccd4,#5a6472)}
.ph-c{background:linear-gradient(#645a52,#2b2522)}
.ph-d{background:linear-gradient(#5a544f,#23201e)}
.jcard h4{font-size:7px;font-weight:600;margin:10px 0 4px;line-height:1.4}
.jcard a{font-size:5.5px;color:var(--blue)}
.jstack{display:flex;flex-direction:column;gap:8px}
.jsmall{width:130px;height:91px;border-radius:5px;position:relative;text-align:left;padding:48px 30px 0 12px;color:#fff;font-size:7px;font-weight:500;line-height:1.4}
.jsmall::after{content:"";position:absolute;right:8px;bottom:12px;width:13px;height:13px;border-radius:50%;background:var(--blue);border:1px solid #fff}
.jam .btn{margin-top:18px;padding:7px 18px}

/* cta */
.cta{height:151px;background:#dfeafb;display:flex}
.cta-half{flex:1;padding:30px 22px 0;text-align:center}
.cta-half + .cta-half{background:#cfe0f9;padding-top:36px}
.cta h3{font-size:9.5px;color:var(--blue-dark);line-height:1.35}
.cta p{margin:6px 0 7px;font-size:5.3px}
.blueprint{display:flex;gap:8px;align-items:center}
.book{width:46px;height:38px;border:2px solid var(--navy);border-radius:2px;background:linear-gradient(#1f3f87,#0c1a3d);flex:none}

/* footer */
.footer{height:180px;background:var(--black);position:relative;color:#fff;padding:40px 46px 0}
.foot-cols{display:flex;gap:26px}
.foot-logo{width:214px}
.foot-logo .logo{font-size:15px;font-weight:500}
.foot-logo .logo .dot{width:22px;height:22px}
.socials{display:flex;gap:6px;margin:14px 0 0 80px}
.socials span{width:9px;height:9px;border-radius:50%;background:#fff}
.socials span:first-child{background:var(--blue)}
.footer h4{font-family:"Montserrat",sans-serif;font-size:7.5px;font-weight:500;letter-spacing:.06em;margin-bottom:10px;white-space:nowrap}
.footer ul{list-style:none;font-size:5.5px;line-height:2.2;white-space:nowrap}
.footer li::before{content:"« ";}
.news{width:116px}
.news .input{height:16px;border:1px solid #333;font-size:4.5px;color:#888;padding:5px}
.news .btn{display:block;text-align:center;margin-top:6px;background:var(--blue-dark)}
.copyright{position:absolute;left:0;right:0;bottom:24px;text-align:center;font-size:5px;color:#ccc}
.copyright a{color:var(--blue)}
</style>
</head>
<body>

<main class="page page--form">
  <header class="nav">
    <div class="logo"><span class="dot"></span>BenefitGavelHub</div>
    <nav class="nav-links"><span>How It Works</span><span>Pricing</span><span>About</span><span>Blog</span></nav>
    <span class="search"></span>
    <span class="btn btn--navy">For Bidders</span>
    <span class="btn">For Fundraisers</span>
  </header>

  <section class="hero">
    <div class="hero-bg" role="img" aria-label="Bright blue backdrop with a person holding a phone"></div>
    <div class="hero-copy">
      <h1>You've just found the easiest online auction platform to use, period</h1>
      <p>BenefitGavelHub has eliminated the headache of setting up online and in-person auctions. We've simplified everything to get you up and running quickly without the help of a tech team.</p>
      <div class="hero-actions"><span class="btn">Online Auctions</span><span class="btn btn--navy">Live In-Person Auctions</span><span class="btn btn--light">Mobile Auctions</span></div>
    </div>
    <form class="event-card">
      <h3>Create Event</h3>
      <div class="field field--text">Name your event</div>
      <div class="field field--text">Event Benefits</div>
      <div class="field">Country*</div>
      <div class="field">Time Zone*</div>
      <div class="field">Currency*</div>
      <span class="link">CREATE NEW EVENT</span>
    </form>
  </section>

  <section class="categories">
    <h2 class="section-title"><span class="dot"></span>Categories</h2>
    <div class="cat-row">
      <div class="cat"><svg viewBox="0 0 24 24" fill="none" stroke="#2f7de1" stroke-width="1.3"><path d="M12 20s-7-4.5-7-10a4 4 0 0 1 7-2.5A4 4 0 0 1 19 10c0 5.5-7 10-7 10z"/></svg><span>Nonprofits<br>Charities</span></div>
      <div class="cat"><svg viewBox="0 0 24 24" fill="none" stroke="#2f7de1" stroke-width="1.3"><path d="M3 20h18M5 20V10h14v10M3 10l9-6 9 6M10 20v-5h4v5"/></svg><span>Schools<br>Education</span></div>
      <div class="cat"><svg viewBox="0 0 24 24" fill="none" stroke="#2f7de1" stroke-width="1.3"><circle cx="12" cy="12" r="7"/><path d="M5 12h14M12 5v14"/></svg><span>Businesses</span></div>
      <div class="cat"><svg viewBox="0 0 24 24" fill="none" stroke="#2f7de1" stroke-width="1.3"><path d="M3 20h18M5 17h14M6 17v-7M10 17v-7M14 17v-7M18 17v-7M4 10h16L12 4z"/></svg><span>Government<br>Agencies</span></div>
      <div class="cat"><svg viewBox="0 0 24 24" fill="none" stroke="#2f7de1" stroke-width="1.3"><circle cx="12" cy="7" r="3"/><path d="M5 20c0-4 3-6 7-6s7 2 7 6"/></svg><span>Individuals</span></div>
    </div>
  </section>

  <section class="spend-title"><h2 class="section-title"><span class="dot"></span>Spend less time. Make more money.</h2></section>

  <section class="row row--b1">
    <div class="circle"><div class="img-donate" role="img" aria-label="Hand holding a tablet showing a donate screen"></div></div>
    <div class="copy">
      <h3>Quickly create, design and manage auctions.</h3>
      <p>You are only 5 minutes away from having your auction built and ready for items. We took the pain and confusion out of getting started.</p>
      <div class="quote"><span class="avatar" role="img" aria-label="Customer portrait"></span><div class="stars">★★★★★</div><p>"I'm 74 years old and I didn't need to call my Grandkids to set up this auction for me! The software was easy to use and the end of auction experience was a breeze!"</p><div class="who"><b>Marion K.</b> - Lakeview Service Club</div></div>
      <span class="btn">Build an auction</span>
    </div>
  </section>

  <section class="row row--b2">
    <div class="copy">
      <h3>More money goes directly<br>to your cause.</h3>
      <p>You can accept cash, checks, bank transfers, or credit cards. It's your money, collect it on your own terms.</p>
      <div class="quote"><span class="avatar" role="img" aria-label="Customer portrait"></span><div class="stars">★★★★★</div><p>"We just completed an auction that raised over $30,000 for a family battling cancer. The platform made it possible with very little cost. 100% we will use them again."</p><div class="who"><b>Daniel Foster</b> - Hartwell Family Fund</div></div>
      <span class="btn">Collect more money</span>
    </div>
    <div class="circle"><div class="img-phone" role="img" aria-label="Hand holding a phone photographing an auction item"></div></div>
  </section>

  <div class="kids" role="img" aria-label="Faded photo of smiling children raising their hands">
    <section class="row row--b3">
      <div class="circle"><div class="img-tablet" role="img" aria-label="Tablet and phone showing a make a donation screen"></div></div>
      <div class="copy">
        <h3>Manage your donors and donations effortlessly.</h3>
        <p>Our Donation CRM allows you to easily track all donations and donors in an easy-to-use dashboard. Export all information or sync with our integration partners to unlock more donor management tools.</p>
        <div class="quote"><span class="avatar" role="img" aria-label="Customer portrait"></span><div class="stars">★★★★★</div><p>"The people coming to our events say it's easy to use and we can check people out so much faster than we ever could in the past. I highly recommend trying this platform out, you'll never go anywhere else."</p><div class="who"><b>Greg Ostrow</b> - Lakeshore Runners</div></div>
        <span class="btn">Manage my donors</span>
      </div>
    </section>
    <section class="company">
      <h2 class="section-title"><span class="dot"></span>You're in good company</h2>
      <p class="sub">Here are some other organizations that have run auctions with us:</p>
      <div class="partners"><div class="partner"></div><div class="partner partner--card"><span></span></div><div class="partner"></div><div class="partner"></div></div>
    </section>
  </div>

  <section class="features">
    <h2 class="section-title"><span class="dot"></span>Most used features</h2>
    <div class="tabs"><span class="tab tab--on">Online Auctions</span><span class="tab">Mobile Hybrid Auctions</span><span class="tab">Live In-Person Auctions</span><span class="tab">Chance Auctions</span><span class="tab">Raffle/Ticket Sales</span></div>
    <div class="feat-body">
      <div class="diamond"><div class="shape"></div><div class="photo" role="img" aria-label="Man smiling while using a laptop"></div></div>
      <div class="feat-copy">
        <h3>Online Auctions</h3>
        <p>Lorem ipsum dolor sit amet, consectetur adipiscing elit, sed do eiusmod tempor incididunt ut labore et dolore magna aliqua. Quis ipsum suspendisse ultrices gravida. Risus commodo viverra maecenas accumsan lacus vel facilisis.</p>
        <p>Lorem ipsum dolor sit amet, consectetur adipiscing elit, sed do eiusmod tempor incididunt ut labore et dolore magna aliqua. Quis ipsum suspendisse ultrices gravida. Risus commodo viverra maecenas accumsan lacus vel facilisis.</p>
        <p>Lorem ipsum dolor sit amet, consectetur adipiscing elit, sed do eiusmod tempor incididunt ut labore et dolore magna aliqua. Quis ipsum suspendisse ultrices gravida. Risus commodo viverra maecenas accumsan lacus vel facilisis.</p>
        <span class="btn">Learn more</span>
      </div>
    </div>
  </section>

  <section class="faq">
    <h2 class="section-title"><span class="dot"></span>Frequently asked questions</h2>
    <div class="faq-card">
      <div class="q"><b>01</b>Can I Pass Fees Onto Bidders?<i>+</i></div>
      <div class="q"><b>02</b>What Happens If Items Don't Sell?<i>+</i></div>
      <div class="q"><b>03</b>Can I Download All My Bidder Data?<i>+</i></div>
      <div class="q q--open"><b>04</b>What Is The Management Fee?<i>–</i></div>
      <div class="answer"><p>The management fee is a fee we charge to use our platform. If you select our free plan, we will charge a 5% management fee of the total amount raised. For example, if your auction raises $1000, we will collect a $50 management fee. Depending on your auction goals and size, you could limit management fees by choosing a prepaid plan. <a>Read More</a></p></div>
      <span class="chev"></span>
    </div>
  </section>

  <section class="support" role="img" aria-label="Smiling support agent wearing a headset in an office">
    <span class="dot"></span>
    <h2>Friendly technical support and training when you need it.</h2>
    <p>Other companies charge hundreds of dollars for your auction support and training. We offer it for free.</p>
    <span class="btn btn--red">Schedule a call</span>
  </section>

  <section class="jam">
    <h2 class="section-title"><span class="dot"></span>Your auction come jam packed with all<br>the features for live events</h2>
    <div class="jam-grid">
      <div class="jcard"><div class="ph ph-a" role="img" aria-label="Woman with arms crossed"></div><h4>Lorem ipsum dolor sit amet, consectetur adipiscing</h4><p>Lorem ipsum dolor sit amet, consectetur adipiscing elit</p><a>Learn More →</a></div>
      <div class="jcard"><div class="ph ph-b" role="img" aria-label="Hands typing on a laptop"></div><h4>Lorem ipsum dolor sit amet, consectetur adipiscing</h4><p>Lorem ipsum dolor sit amet, consectetur adipiscing elit</p><a>Learn More →</a></div>
      <div class="jstack">
        <div class="jsmall ph-c" role="img" aria-label="Person talking on a phone">Lorem ipsum dolor sit amet,</div>
        <div class="jsmall ph-d" role="img" aria-label="Man using a laptop on a sofa">Lorem ipsum dolor sit amet,</div>
      </div>
    </div>
    <span class="btn btn--round">View more</span>
  </section>

  <section class="cta">
    <div class="cta-half">
      <div class="blueprint">
        <div><h3>Download the auction growth playbook</h3><p>Learn the 4 tools BIG Organizations use to skyrocket their auction profits! Stop leaving thousands of dollars on the table by following this Step-By-Step Guide.</p><span class="btn">Download guide</span></div>
        <div class="book" role="img" aria-label="Auction growth playbook guide cover"></div>
      </div>
    </div>
    <div class="cta-half"><h3>Let's get started, it's super easy.</h3><p>Oh yeah, you don't need a credit card to get started either.</p><span class="btn">Build an auction</span></div>
  </section>

  <footer class="footer">
    <div class="foot-cols">
      <div class="foot-logo"><div class="logo"><span class="dot"></span>BenefitGavelHub</div><div class="socials"><span></span><span></span><span></span><span></span></div></div>
      <div><h4>Help Links</h4><ul><li>Terms &amp; Conditions</li><li>Privacy Policy</li><li>About Us</li><li>Support</li></ul></div>
      <div class="news"><h4>Get our newsletter</h4><div class="input">Enter Your Email</div><span class="btn">Subscribe now</span></div>
    </div>
    <div class="copyright">©Copyrights 2023 <a>BenefitGavelHub</a> | All Rights Reserved</div>
  </footer>
</main>

<main class="page page--photo">
  <header class="nav">
    <div class="logo"><span class="dot"></span>BenefitGavelHub</div>
    <nav class="nav-links"><span>How It Works</span><span>Pricing</span><span>About</span><span>Blog</span></nav>
    <span class="search"></span>
    <span class="btn btn--navy">For Bidders</span>
    <span class="btn">For Fundraisers</span>
  </header>

  <section class="hero">
    <div class="hero-bg" role="img" aria-label="Excited woman celebrating in front of a laptop on a sofa"></div>
    <div class="hero-copy">
      <h1>You've just found the easiest online auction platform to use, period</h1>
      <p>BenefitGavelHub has eliminated the headache of setting up online and in-person auctions. We've simplified everything to get you up and running quickly without the help of a tech team.</p>
      <div class="hero-actions"><span class="btn">Online Auctions</span><span class="btn btn--navy">Live In-Person Auctions</span><span class="btn btn--light">Mobile Auctions</span></div>
    </div>
  </section>

  <section class="categories">
    <h2 class="section-title"><span class="dot"></span>Categories</h2>
    <div class="cat-row">
      <div class="cat"><svg viewBox="0 0 24 24" fill="none" stroke="#2f7de1" stroke-width="1.3"><path d="M12 20s-7-4.5-7-10a4 4 0 0 1 7-2.5A4 4 0 0 1 19 10c0 5.5-7 10-7 10z"/></svg><span>Nonprofits<br>Charities</span></div>
      <div class="cat"><svg viewBox="0 0 24 24" fill="none" stroke="#2f7de1" stroke-width="1.3"><path d="M3 20h18M5 20V10h14v10M3 10l9-6 9 6M10 20v-5h4v5"/></svg><span>Schools<br>Education</span></div>
      <div class="cat"><svg viewBox="0 0 24 24" fill="none" stroke="#2f7de1" stroke-width="1.3"><circle cx="12" cy="12" r="7"/><path d="M5 12h14M12 5v14"/></svg><span>Businesses</span></div>
      <div class="cat"><svg viewBox="0 0 24 24" fill="none" stroke="#2f7de1" stroke-width="1.3"><path d="M3 20h18M5 17h14M6 17v-7M10 17v-7M14 17v-7M18 17v-7M4 10h16L12 4z"/></svg><span>Government<br>Agencies</span></div>
      <div class="cat"><svg viewBox="0 0 24 24" fill="none" stroke="#2f7de1" stroke-width="1.3"><circle cx="12" cy="7" r="3"/><path d="M5 20c0-4 3-6 7-6s7 2 7 6"/></svg><span>Individuals</span></div>
    </div>
  </section>

  <section class="spend-title"><h2 class="section-title"><span class="dot"></span>Spend less time. Make more money.</h2></section>

  <section class="row row--b1">
    <div class="circle"><div class="img-donate" role="img" aria-label="Hand holding a tablet showing a donate screen"></div></div>
    <div class="copy">
      <h3>Quickly create, design and manage auctions.</h3>
      <p>You are only 5 minutes away from having your auction built and ready for items. We took the pain and confusion out of getting started.</p>
      <div class="quote"><span class="avatar" role="img" aria-label="Customer portrait"></span><div class="stars">★★★★★</div><p>"I'm 74 years old and I didn't need to call my Grandkids to set up this auction for me! The software was easy to use and the end of auction experience was a breeze!"</p><div class="who"><b>Marion K.</b> - Lakeview Service Club</div></div>
      <span class="btn">Build an auction</span>
    </div>
  </section>

  <section class="row row--b2">
    <div class="copy">
      <h3>More money goes directly<br>to your cause.</h3>
      <p>You can accept cash, checks, bank transfers, or credit cards. It's your money, collect it on your own terms.</p>
      <div class="quote"><span class="avatar" role="img" aria-label="Customer portrait"></span><div class="stars">★★★★★</div><p>"We just completed an auction that raised over $30,000 for a family battling cancer. The platform made it possible with very little cost. 100% we will use them again."</p><div class="who"><b>Daniel Foster</b> - Hartwell Family Fund</div></div>
      <span class="btn">Collect more money</span>
    </div>
    <div class="circle"><div class="img-phone" role="img" aria-label="Hand holding a phone photographing an auction item"></div></div>
  </section>

  <div class="kids" role="img" aria-label="Faded photo of smiling children raising their hands">
    <section class="row row--b3">
      <div class="circle"><div class="img-tablet" role="img" aria-label="Tablet and phone showing a make a donation screen"></div></div>
      <div class="copy">
        <h3>Manage your donors and donations effortlessly.</h3>
        <p>Our Donation CRM allows you to easily track all donations and donors in an easy-to-use dashboard. Export all information or sync with our integration partners to unlock more donor management tools.</p>
        <div class="quote"><span class="avatar" role="img" aria-label="Customer portrait"></span><div class="stars">★★★★★</div><p>"The people coming to our events say it's easy to use and we can check people out so much faster than we ever could in the past. I highly recommend trying this platform out, you'll never go anywhere else."</p><div class="who"><b>Greg Ostrow</b> - Lakeshore Runners</div></div>
        <span class="btn">Manage my donors</span>
      </div>
    </section>
    <section class="company">
      <h2 class="section-title"><span class="dot"></span>You're in good company</h2>
      <p class="sub">Here are some other organizations that have run auctions with us:</p>
      <div class="partners"><div class="partner"></div><div class="partner partner--card"><span></span></div><div class="partner"></div><div class="partner"></div></div>
    </section>
  </div>

  <section class="features">
    <h2 class="section-title"><span class="dot"></span>Most used features</h2>
    <div class="tabs"><span class="tab tab--on">Online Auctions</span><span class="tab">Mobile Hybrid Auctions</span><span class="tab">Live In-Person Auctions</span><span class="tab">Chance Auctions</span><span class="tab">Raffle/Ticket Sales</span></div>
    <div class="feat-body">
      <div class="diamond"><div class="shape"></div><div class="photo" role="img" aria-label="Man smiling while using a laptop"></div></div>
      <div class="feat-copy">
        <h3>Online Auctions</h3>
        <p>Lorem ipsum dolor sit amet, consectetur adipiscing elit, sed do eiusmod tempor incididunt ut labore et dolore magna aliqua. Quis ipsum suspendisse ultrices gravida. Risus commodo viverra maecenas accumsan lacus vel facilisis.</p>
        <p>Lorem ipsum dolor sit amet, consectetur adipiscing elit, sed do eiusmod tempor incididunt ut labore et dolore magna aliqua. Quis ipsum suspendisse ultrices gravida. Risus commodo viverra maecenas accumsan lacus vel facilisis.</p>
        <p>Lorem ipsum dolor sit amet, consectetur adipiscing elit, sed do eiusmod tempor incididunt ut labore et dolore magna aliqua. Quis ipsum suspendisse ultrices gravida. Risus commodo viverra maecenas accumsan lacus vel facilisis.</p>
        <span class="btn">Learn more</span>
      </div>
    </div>
  </section>

  <section class="faq">
    <h2 class="section-title"><span class="dot"></span>Frequently asked questions</h2>
    <div class="faq-card">
      <div class="q"><b>01</b>Can I Pass Fees Onto Bidders?<i>+</i></div>
      <div class="q"><b>02</b>What Happens If Items Don't Sell?<i>+</i></div>
      <div class="q"><b>03</b>Can I Download All My Bidder Data?<i>+</i></div>
      <div class="q q--open"><b>04</b>What Is The Management Fee?<i>–</i></div>
      <div class="answer"><p>The management fee is a fee we charge to use our platform. If you select our free plan, we will charge a 5% management fee of the total amount raised. For example, if your auction raises $1000, we will collect a $50 management fee. Depending on your auction goals and size, you could limit management fees by choosing a prepaid plan. <a>Read More</a></p></div>
      <span class="chev"></span>
    </div>
  </section>

  <section class="support" role="img" aria-label="Smiling support agent wearing a headset in an office">
    <span class="dot"></span>
    <h2>Friendly technical support and training when you need it.</h2>
    <p>Other companies charge hundreds of dollars for your auction support and training. We offer it for free.</p>
    <span class="btn btn--red">Schedule a call</span>
  </section>

  <section class="jam">
    <h2 class="section-title"><span class="dot"></span>Your auction come jam packed with all<br>the features for live events</h2>
    <div class="jam-grid">
      <div class="jcard"><div class="ph ph-a" role="img" aria-label="Woman with arms crossed"></div><h4>Lorem ipsum dolor sit amet, consectetur adipiscing</h4><p>Lorem ipsum dolor sit amet, consectetur adipiscing elit</p><a>Learn More →</a></div>
      <div class="jcard"><div class="ph ph-b" role="img" aria-label="Hands typing on a laptop"></div><h4>Lorem ipsum dolor sit amet, consectetur adipiscing</h4><p>Lorem ipsum dolor sit amet, consectetur adipiscing elit</p><a>Learn More →</a></div>
      <div class="jstack">
        <div class="jsmall ph-c" role="img" aria-label="Person talking on a phone">Lorem ipsum dolor sit amet,</div>
        <div class="jsmall ph-d" role="img" aria-label="Man using a laptop on a sofa">Lorem ipsum dolor sit amet,</div>
      </div>
    </div>
    <span class="btn btn--round">View more</span>
  </section>

  <section class="cta">
    <div class="cta-half">
      <div class="blueprint">
        <div><h3>Download the auction growth playbook</h3><p>Learn the 4 tools BIG Organizations use to skyrocket their auction profits! Stop leaving thousands of dollars on the table by following this Step-By-Step Guide.</p><span class="btn">Download guide</span></div>
        <div class="book" role="img" aria-label="Auction growth playbook guide cover"></div>
      </div>
    </div>
    <div class="cta-half"><h3>Let's get started, it's super easy.</h3><p>Oh yeah, you don't need a credit card to get started either.</p><span class="btn">Build an auction</span></div>
  </section>

  <footer class="footer">
    <div class="foot-cols">
      <div class="foot-logo"><div class="logo"><span class="dot"></span>BenefitGavelHub</div><div class="socials"><span></span><span></span><span></span><span></span></div></div>
      <div><h4>Help Links</h4><ul><li>Terms &amp; Conditions</li><li>Privacy Policy</li><li>About Us</li><li>Support</li></ul></div>
      <div class="news"><h4>Get our newsletter</h4><div class="input">Enter Your Email</div><span class="btn">Subscribe now</span></div>
    </div>
    <div class="copyright">©Copyrights 2023 <a>BenefitGavelHub</a> | All Rights Reserved</div>
  </footer>
</main>

</body>
</html>
```